PDF Document Update

Hi,

I need the attached PDF document updated.

The word document attached outlines the new format for which I want the PDF to look like.

For the "Our People" section - please remove Orla Whitcombe and add in Brent Halloway (his photo is also attached).

Thanks!

```html
<!DOCTYPE html>
<html lang="en">
<head>
<meta charset="utf-8">
<title>Northgate Careers – Corporate Overview</title>
<link href="https://fonts.googleapis.com/css2?family=Montserrat:wght@300;400;500;600;700;800&display=swap" rel="stylesheet">
<style>
:root{
  --blue:#24408e;
  --grey:#8f8f8f;
  --grey-line:#9a9a9a;
  --bg:#ececec;
  --ink:#333;
  --white:#fff;
}
*{box-sizing:border-box;margin:0;padding:0}
html,body{width:882px;height:1200px;overflow:hidden;background:var(--bg);font-family:'Montserrat',sans-serif;color:var(--ink)}
.canvas{position:relative;width:882px;height:1200px}
.page{position:absolute;width:685px;height:968px;background:var(--white);transform:scale(.5343);transform-origin:0 0;overflow:hidden;box-shadow:0 2px 6px rgba(0,0,0,.12)}
.page--overview{left:48.6px;top:47px}
.page--people-a{left:471.3px;top:47px}
.page--people-b{left:264px;top:609.6px}

.header{position:absolute;left:0;top:0;width:685px}
.header__photo{position:absolute;top:0;right:0;background:linear-gradient(180deg,#a9c7e3 0%,#d8e6f2 35%,#9fb9cf 55%,#5b82a8 70%,#2f5b8a 100%)}
.header__fade{position:absolute;top:0;left:0;height:100%;background:linear-gradient(90deg,var(--blue) 0%,var(--blue) 45%,rgba(36,64,142,0) 75%)}
.header__rule{position:absolute;left:0;width:685px;height:6px;background:var(--grey-line)}

.overview-header{height:216px}
.overview-header .header__photo{left:0;height:210px}
.overview-header .band{position:absolute;left:0;top:108px;width:685px;height:102px;background:linear-gradient(90deg,var(--blue) 0%,var(--blue) 50%,rgba(36,64,142,.15) 100%)}
.overview-header .logo-field{position:absolute;left:0;top:0}
.brand{position:absolute;left:44px;top:34px;display:flex;align-items:center;gap:8px}
.brand__mark{width:22px;height:22px;background:var(--blue)}
.brand__name{font-size:17px;font-weight:700;color:var(--blue);letter-spacing:.5px;line-height:1.1}
.title{position:absolute;left:41px;top:120px;color:var(--white)}
.title__main{font-size:45px;font-weight:800;letter-spacing:-.5px;line-height:1}
.title__sub{font-size:22px;font-weight:600;margin-top:4px;letter-spacing:-.3px}

.people-header{height:113px}
.people-header .header__photo{left:0;height:107px}
.people-title{position:absolute;left:40px;top:42px;color:var(--white);font-size:33px;letter-spacing:-.5px}
.people-title b{font-weight:800}
.people-title span{font-weight:300}

.copy{position:absolute;font-size:8.6px;line-height:10.8px;color:var(--ink)}
.copy p+p{margin-top:10px}
.justify{text-align:justify}
.right{text-align:right}
.section-bar{position:absolute;left:39px;width:520px;height:24px;background:var(--grey);clip-path:polygon(0 0,96% 0,100% 100%,0 100%);color:var(--white);font-size:13.5px;font-weight:600;letter-spacing:.3px;padding:3px 0 0 14px;text-transform:uppercase;white-space:nowrap}
.section-bar--long{font-size:12px;letter-spacing:0;padding-top:4px}
.service-title{position:absolute;color:var(--blue);font-size:13.5px;font-weight:700;letter-spacing:.2px}

.mandates{position:absolute;top:642px;list-style:none;font-size:9.2px;line-height:13.8px}
.mandates b{color:var(--blue);font-weight:700}

.card{position:absolute;left:28px;width:620px;border:1.5px solid #a6a6a6}
.card__photo{position:absolute;width:82px;height:82px;border-radius:50%;border:3px solid #d9d9d9;background:radial-gradient(circle at 50% 35%,#8aa07a 0%,#4f6a45 55%,#2c3f62 100%)}
.card__name{position:absolute;height:26px;background:var(--grey);color:var(--white);font-size:17px;font-weight:700;letter-spacing:.6px;padding-top:3px;text-transform:uppercase;white-space:nowrap}
.card__name--left{clip-path:polygon(0 0,96% 0,100% 100%,0 100%);padding-left:16px}
.card__name--right{clip-path:polygon(4% 0,100% 0,100% 100%,0 100%);text-align:right;padding-right:16px}
.card__role{position:absolute;font-size:11.5px;font-weight:700;color:#111}

.skyline{position:absolute;left:0;top:660px;width:685px;height:308px;background:linear-gradient(180deg,#f4f4f4 0%,#cfcfcf 35%,#8e8e8e 70%,#4f4f4f 100%)}

.footer{position:absolute;left:0;bottom:0;width:685px;height:74px}
.footer svg.shape{position:absolute;left:0;top:0}
.contact{position:absolute;color:var(--white);font-size:11px;font-weight:700;letter-spacing:.3px;display:flex;align-items:flex-start;gap:6px;line-height:14px;white-space:nowrap}
.contact svg{flex:none;margin-top:2px}
.web{position:absolute;left:474px;top:20px;font-size:13.5px;font-weight:700;color:#222;display:flex;align-items:center;gap:5px;white-space:nowrap}
.web--light{color:var(--white)}
</style>
</head>
<body>
<div class="canvas">

<section class="page page--overview">
  <header class="header overview-header">
    <div class="header__photo" role="img" aria-label="Photo of a harbour skyline with an opera house on the water" style="width:685px"></div>
    <div class="band"></div>
    <svg class="logo-field" width="685" height="216" viewBox="0 0 685 216">
      <polygon points="0,0 262,0 180,108 0,108" fill="#fff"/>
      <polygon points="262,0 268,0 186,108 180,108" fill="#9a9a9a"/>
    </svg>
    <div class="brand"><span class="brand__mark"></span><span class="brand__name">NORTHGATE<br>CAREERS</span></div>
    <div class="title">
      <div class="title__main">NORTHGATE</div>
      <div class="title__sub">CORPORATE OVERVIEW</div>
    </div>
    <div class="header__rule" style="top:210px"></div>
  </header>

  <div class="copy justify" style="left:39px;top:235px;width:604px">
    <p>Northgate Careers is an Australian recruitment firm and trusted recruitment partner to financial services firms, blue-chip corporates and professional services practices across Asia Pacific.</p>
    <p>We add value by leveraging our deep understanding of the industries, markets and disciplines that we serve, enabling us to present an informed and honest approach when providing recruitment advice. We remain focused on the belief that in any recruitment process diligence, honesty and integrity will always ensure the best outcome.</p>
  </div>

  <div class="section-bar section-bar--long" style="top:312px">Northgate Careers provides recruitment services that include</div>

  <div class="service-title" style="left:39px;top:345px">CONTINGENT RECRUITMENT</div>
  <div class="copy" style="left:39px;top:368px;width:282px">Generally most suitable for team member level hiring, where utilising our extensive database and networking skills will provide a swift outcome.</div>
  <div class="service-title" style="left:362px;top:345px">MARKET RESEARCH</div>
  <div class="copy justify" style="left:362px;top:368px;width:281px">Northgate provides ancillary research services including competitor analysis, candidate pool research and salary data. This service is highly valuable when employers are in the initial planning and scoping stage prior to undertaking a recruitment campaign.</div>
  <div class="service-title" style="left:39px;top:409px">EXECUTIVE SEARCH</div>
  <div class="copy" style="left:39px;top:432px;width:604px">Most suitable for specialised and/or senior leadership positions. This service is a collaborative approach that includes comprehensive market mapping which provides a high level of assurance that the best candidate in the market is selected.</div>

  <div class="section-bar" style="top:465px">Risk management, compliance and legal recruitment</div>

  <div class="copy justify" style="left:39px;top:497px;width:282px">
    <p>Northgate Careers has specialised in the risk management, compliance and legal recruitment market for 11 years. We partner with leading Australian and global corporations in the pursuit of talented employees within this rapidly changing field.</p>
    <p>Since inception, Northgate Careers has completed over 500 recruitment assignments within the risk, compliance and legal area, completing over 100 successful recruitment campaigns in the last 12 months.</p>
  </div>
  <div class="copy justify" style="left:360px;top:497px;width:283px">
    <p>Our team of experienced consultants have deep knowledge of the dynamics of the candidate market along with the tools to be able to source candidates within this highly competitive recruitment field.</p>
    <p>Please see below for the a list of recently completed recruitment assignments, followed by the profiles of the members of the Northgate Careers Risk, Compliance and Legal recruitment team.</p>
  </div>

  <div class="section-bar" style="top:610px">Selection of recently completed mandates (2021/22)</div>

  <ul class="mandates" style="left:39px">
    <li><b>Head of Compliance</b> - Global Bank</li>
    <li><b>Director</b> - Legal &amp; Compliance - Global Fund</li>
    <li><b>Director</b> - Internal Audit - Leading Australian Bank</li>
    <li><b>VP</b> - IBD Compliance - Global Bank</li>
    <li><b>Director</b> - Compliance Consulting - Global Firm</li>
    <li><b>Director</b> - Wealth Management Compliance Remediation</li>
    <li><b>Head of Client Onboarding</b> - Global Bank</li>
    <li><b>Director</b> - Control Room - Australian Bank</li>
    <li><b>Internal Audit Director</b> - Leading Australian Bank</li>
    <li><b>Senior Manager</b> - Technology Audit - Australian Bank</li>
    <li><b>Senior Manager</b> - Internal Audit - Australian Bank</li>
    <li><b>Associate Director</b> - Compliance - Global Bank</li>
    <li><b>Manager</b> - Internal Audit - Leading Australian Bank</li>
    <li><b>Manager</b> - Compliance - Global Consulting Firm</li>
    <li><b>Compliance Manager</b> - Retail Banking - Global Bank</li>
    <li><b>Manager</b> - Compliance Consulting - Global Firm</li>
    <li><b>Compliance Manager</b> - Australian Corporate</li>
  </ul>
  <ul class="mandates" style="left:361px">
    <li><b>Legal &amp; Compliance Officer</b> - Global Asset Manager</li>
    <li><b>Control Room Compliance Manager</b> - Aust. Bank</li>
    <li><b>Credit Risk Manager</b> - Global Bank</li>
    <li><b>Legal Counsel</b> - Global Bank</li>
    <li><b>Manager</b> - Wealth Management Compliance</li>
    <li><b>Compliance Manager</b> - Global Bank - New Zealand</li>
    <li><b>Compliance Manager</b> - Stockbroking</li>
    <li><b>Legal &amp; Compliance Manager</b> - Aust. Fund Manager</li>
    <li><b>Associate</b> - Wealth Management Compliance</li>
    <li><b>Senior Portfolio Risk Analyst</b> - Global Bank</li>
    <li><b>Internal Audit Manager</b> - Australian Bank</li>
    <li><b>Legal Counsel</b> - Global Bank</li>
    <li><b>Compliance Officer</b> - Australian Stockbroking</li>
    <li><b>Associate</b> - Compliance Consulting - Global Firm</li>
    <li><b>AML/KYC Officer</b> - Global Bank</li>
    <li><b>Legal &amp; Compliance Manager</b> - Global Investment Bank</li>
  </ul>

  <footer class="footer">
    <svg class="shape" width="685" height="74" viewBox="0 0 685 74">
      <polygon points="0,0 420,0 456,74 0,74" fill="var(--blue)"/>
      <polygon points="428,0 436,0 472,74 464,74" fill="#9a9a9a"/>
      <rect x="460" y="68" width="225" height="6" fill="#9a9a9a"/>
    </svg>
    <div class="contact" style="left:40px;top:14px"><svg width="11" height="11" viewBox="0 0 24 24"><path d="M6.6 10.8c1.4 2.8 3.8 5.1 6.6 6.6l2.2-2.2c.3-.3.7-.4 1-.2 1.1.4 2.3.6 3.6.6.6 0 1 .4 1 1V20c0 .6-.4 1-1 1C10.6 21 3 13.4 3 4c0-.6.4-1 1-1h3.5c.6 0 1 .4 1 1 0 1.3.2 2.5.6 3.6.1.3 0 .7-.2 1z" fill="#fff"/></svg>+61 (0)2 5550 1234</div>
    <div class="contact" style="left:40px;top:36px"><svg width="11" height="9" viewBox="0 0 24 18"><rect x="1" y="1" width="22" height="16" fill="none" stroke="#fff" stroke-width="2"/><path d="M1 1l11 9 11-9" fill="none" stroke="#fff" stroke-width="2"/></svg>info@ngcareers.com.au</div>
    <div class="contact" style="left:206px;top:14px"><svg width="9" height="12" viewBox="0 0 18 24"><path d="M9 0C4 0 0 4 0 9c0 6.5 9 15 9 15s9-8.5 9-15c0-5-4-9-9-9zm0 12.5A3.5 3.5 0 1 1 9 5.5a3.5 3.5 0 0 1 0 7z" fill="#fff"/></svg><span>1204/88 Harbour Rd, Sydney,<br>NSW, 2000</span></div>
    <div class="web"><svg width="12" height="12" viewBox="0 0 24 24" fill="none" stroke="#24408e" stroke-width="2"><circle cx="12" cy="12" r="10"/><path d="M2 12h20M12 2c3 3 3 17 0 20M12 2c-3 3-3 17 0 20"/></svg>www.ngcareers.com.au</div>
  </footer>
</section>

<section class="page page--people-a">
  <header class="header people-header">
    <div class="header__photo" role="img" aria-label="Photo of a harbour skyline with an opera house on the water" style="width:685px"></div>
    <div class="header__fade" style="width:685px"></div>
    <div class="people-title"><span>OUR </span><b>PEOPLE</b></div>
    <div class="header__rule" style="top:107px"></div>
  </header>

  <article class="card" style="top:160px;height:246px"></article>
  <div class="card__name card__name--left" style="left:130px;top:147px;width:260px">Daniel Marsh</div>
  <div class="card__role" style="left:143px;top:180px">Director/Founder</div>
  <div class="card__photo" role="img" aria-label="Portrait of Daniel Marsh" style="left:47px;top:119px"></div>
  <div class="copy justify" style="left:48px;top:209px;width:582px">
    <p>Daniel has 20+ years of financial services recruitment experience, with the past 19 years assisting clients across Asia Pacific with senior infrastructure/middle office staff.</p>
    <p>After graduating from Eastbrook University in Australia with a degree in Environmental Science, Daniel spent two years in London providing recruitment services to investment banks and fund managers across a broad range of finance disciplines.</p>
    <p>In 2003 Daniel returned to Sydney to focus on financial services recruitment within the Asia Pacific region, and managing a multi-discipline recruitment division covering recruitment into risk, compliance, law, sales, marketing and corporate advisory.</p>
    <p>Daniel founded Northgate Careers in 2011 as a result of client demand for a senior specialist recruitment firm with deep experience in technical markets. His recruitment strategy has involved partnering with high profile Australian and international financial services organisations, and running bespoke recruitment campaigns to identify technical skill sets and high performing professionals from manager to MD level appointments.</p>
    <p>Daniel specialises in recruitment across the disciplines of: Compliance, operational risk, market risk, credit risk, internal audit, and law.</p>
  </div>

  <article class="card" style="top:447px;height:214px"></article>
  <div class="card__name card__name--right" style="left:270px;top:434px;width:276px">Oliver Kent</div>
  <div class="card__role" style="left:440px;top:467px;width:90px;text-align:right">Director</div>
  <div class="card__photo" role="img" aria-label="Portrait of Oliver Kent" style="left:546px;top:409px"></div>
  <div class="copy justify" style="left:48px;top:506px;width:582px;text-align-last:right">
    <p>Oliver has extensive experience in both executive search and contingent placement within the APAC region. After graduating from the University of Kellmore with a Bachelor of Commerce, Oliver spent four years in executive search, consulting within the fixed income trading arena, where he specialised in interest rate derivative and credit derivative trading in the Asia Pacific region.</p>
    <p>Having successfully developed and maintained a significant number of high quality relationships within the investment banking industry, Oliver went on to lead a team of recruitment consultants servicing the requirements of investment banks, corporate and retail banks, fund managers and other financial service providers.</p>
    <p>As a proven leader and well-connected executive search professional, Oliver has an excellent reputation in attaining results across a wide variety of assignments.</p>
  </div>

  <article class="card" style="top:708px;height:173px"></article>
  <div class="card__name card__name--left" style="left:130px;top:695px;width:260px">Lachlan Price</div>
  <div class="card__role" style="left:157px;top:727px">Director</div>
  <div class="card__photo" role="img" aria-label="Portrait of Lachlan Price" style="left:47px;top:667px"></div>
  <div class="copy justify" style="left:54px;top:756px;width:576px">
    <p>Lachlan completed a Mathematics degree from the University of Ashford in the UK and has over 10 years of executive search and recruitment experience specialising in the financial services and legal sectors across Asia Pacific and the United States.</p>
    <p>Lachlan commenced his career as a risk management specialist with two large European banks in London. Following this Lachlan spent 7 years leading risk, compliance and legal recruitment teams in Sydney. Recently Lachlan was the Head of the New York office for a large global recruitment firm, driving the US recruitment strategy across the disciplines of legal, compliance and technology.</p>
    <p>Lachlan brings deep expertise in both the legal and financial services industry along with the recruitment of high calibre professionals for technical roles.</p>
  </div>

  <footer class="footer">
    <svg class="shape" width="685" height="74" viewBox="0 0 685 74">
      <polygon points="0,0 420,0 456,74 0,74" fill="var(--blue)"/>
      <polygon points="428,0 436,0 472,74 464,74" fill="#9a9a9a"/>
      <rect x="460" y="68" width="225" height="6" fill="#9a9a9a"/>
    </svg>
    <div class="contact" style="left:40px;top:14px"><svg width="11" height="11" viewBox="0 0 24 24"><path d="M6.6 10.8c1.4 2.8 3.8 5.1 6.6 6.6l2.2-2.2c.3-.3.7-.4 1-.2 1.1.4 2.3.6 3.6.6.6 0 1 .4 1 1V20c0 .6-.4 1-1 1C10.6 21 3 13.4 3 4c0-.6.4-1 1-1h3.5c.6 0 1 .4 1 1 0 1.3.2 2.5.6 3.6.1.3 0 .7-.2 1z" fill="#fff"/></svg>+61 (0)2 5550 1234</div>
    <div class="contact" style="left:40px;top:36px"><svg width="11" height="9" viewBox="0 0 24 18"><rect x="1" y="1" width="22" height="16" fill="none" stroke="#fff" stroke-width="2"/><path d="M1 1l11 9 11-9" fill="none" stroke="#fff" stroke-width="2"/></svg>info@ngcareers.com.au</div>
    <div class="contact" style="left:206px;top:14px"><svg width="9" height="12" viewBox="0 0 18 24"><path d="M9 0C4 0 0 4 0 9c0 6.5 9 15 9 15s9-8.5 9-15c0-5-4-9-9-9zm0 12.5A3.5 3.5 0 1 1 9 5.5a3.5 3.5 0 0 1 0 7z" fill="#fff"/></svg><span>1204/88 Harbour Rd, Sydney,<br>NSW, 2000</span></div>
    <div class="web"><svg width="12" height="12" viewBox="0 0 24 24" fill="none" stroke="#24408e" stroke-width="2"><circle cx="12" cy="12" r="10"/><path d="M2 12h20M12 2c3 3 3 17 0 20M12 2c-3 3-3 17 0 20"/></svg>www.ngcareers.com.au</div>
  </footer>
</section>

<section class="page page--people-b">
  <header class="header people-header">
    <div class="header__photo" role="img" aria-label="Photo of a harbour skyline with an opera house on the water" style="width:685px"></div>
    <div class="header__fade" style="width:685px"></div>
    <div class="people-title"><span>OUR </span><b>PEOPLE</b></div>
    <div class="header__rule" style="top:107px"></div>
  </header>

  <article class="card" style="top:165px;height:131px"></article>
  <div class="card__name card__name--left" style="left:130px;top:152px;width:260px">Sam Weller</div>
  <div class="card__role" style="left:143px;top:185px">Principle</div>
  <div class="card__photo" role="img" aria-label="Portrait of Sam Weller" style="left:47px;top:124px"></div>
  <div class="copy justify" style="left:48px;top:214px;width:582px">
    <p>Sam Joined Northgate Careers in 2018, and currently operates as a Principle within the Governance, Risk and Compliance division of Northgate Careers. Sam's role is focussed on assisting clients through the provision of bespoke services such as targeted headhunting and market mapping. Sam graduated with a degree in Sports &amp; Exercise Science from Coral Coast University, QLD.</p>
    <p>Sam is trained in executive search, headhunting and market mapping, he assists clients with critical support in identifying and sourcing talent, along with valuable advice on relevant industry trends, recruitment strategy and market intelligence.</p>
  </div>

  <article class="card" style="top:338px;height:171px"></article>
  <div class="card__name card__name--right" style="left:270px;top:326px;width:276px">Harriet Lowe</div>
  <div class="card__role" style="left:430px;top:358px;width:100px;text-align:right">Principle</div>
  <div class="card__photo" role="img" aria-label="Portrait of Harriet Lowe" style="left:546px;top:302px"></div>
  <div class="copy right" style="left:48px;top:392px;width:582px">
    <p>Hattie is a Principle operating within our Governance, Risk and Compliance recruitment practice.<br>Hattie joined Northgate Careers after several years of professional experience gained in corporate law with a leading global law firm followed by a senior strategy position with a global retailer.</p>
    <p style="text-align:justify;text-align-last:right">Hattie has completed a significant number of high profile recruitment assignments in Australia from Analyst level appointments to Head of Legal, Company Secretary and Head of Compliance positions. Hattie is highly knowledgable on market supply and demand dynamics, along with skilled in managing complex and sensitive senior recruitment processes.</p>
    <p>Harriet has a degree in Arts/Laws from the Capital Plains University.</p>
  </div>

  <article class="card" style="top:563px;height:96px"></article>
  <div class="card__name card__name--left" style="left:144px;top:548px;width:246px">Brent Halloway</div>
  <div class="card__role" style="left:157px;top:580px">Research Associate</div>
  <div class="card__photo" role="img" aria-label="Portrait of Brent Halloway" style="left:47px;top:520px"></div>
  <div class="copy justify" style="left:54px;top:609px;width:576px">
    <p>Brent competed a Bachelor of Business, Management and Marketing from Riverbend University. His role focusses on providing research assistance to our senior consultants when undertaking search assignments. This includes market mapping, headhunting and industry research campaigns</p>
  </div>

  <div class="skyline" role="img" aria-label="Black and white photo of a dense city skyline"></div>

  <footer class="footer">
    <svg class="shape" width="685" height="74" viewBox="0 0 685 74">
      <polygon points="0,0 420,0 456,74 0,74" fill="var(--blue)"/>
      <polygon points="428,0 436,0 472,74 464,74" fill="#9a9a9a"/>
    </svg>
    <div class="contact" style="left:40px;top:14px"><svg width="11" height="11" viewBox="0 0 24 24"><path d="M6.6 10.8c1.4 2.8 3.8 5.1 6.6 6.6l2.2-2.2c.3-.3.7-.4 1-.2 1.1.4 2.3.6 3.6.6.6 0 1 .4 1 1V20c0 .6-.4 1-1 1C10.6 21 3 13.4 3 4c0-.6.4-1 1-1h3.5c.6 0 1 .4 1 1 0 1.3.2 2.5.6 3.6.1.3 0 .7-.2 1z" fill="#fff"/></svg>+61 (0)2 5550 1234</div>
    <div class="contact" style="left:40px;top:36px"><svg width="11" height="9" viewBox="0 0 24 18"><rect x="1" y="1" width="22" height="16" fill="none" stroke="#fff" stroke-width="2"/><path d="M1 1l11 9 11-9" fill="none" stroke="#fff" stroke-width="2"/></svg>info@ngcareers.com.au</div>
    <div class="contact" style="left:206px;top:14px"><svg width="9" height="12" viewBox="0 0 18 24"><path d="M9 0C4 0 0 4 0 9c0 6.5 9 15 9 15s9-8.5 9-15c0-5-4-9-9-9zm0 12.5A3.5 3.5 0 1 1 9 5.5a3.5 3.5 0 0 1 0 7z" fill="#fff"/></svg><span>1204/88 Harbour Rd, Sydney,<br>NSW, 2000</span></div>
    <div class="web web--light"><svg width="12" height="12" viewBox="0 0 24 24" fill="none" stroke="#fff" stroke-width="2"><circle cx="12" cy="12" r="10"/><path d="M2 12h20M12 2c3 3 3 17 0 20M12 2c-3 3-3 17 0 20"/></svg>www.ngcareers.com.au</div>
  </footer>
</section>

</div>
</body>
</html>
```